Los Angeles based Demolition, Grading, and Structural concrete Contractor in need of a Sale brochure

We are a Los Angeles-based demolition, grading, and structural concrete contractor looking for a professionally designed sales brochure that represents our company and services. The brochure should be visually appealing, easy to read, and include the following:

-Company Logo: Prominently displayed to enhance brand identity.

-Services We Offer: A clear breakdown of our key services, including demolition, grading, and structural concrete work.

-Project Scope & Capabilities: A brief explanation of the type of projects we handle (residential, commercial, industrial).

-Pricing Information: Mention that demolition services start at $20,000. This price includes complete demolition of structure, safe debris removal and hauling, site preparation for new construction.

-Contact Information: Our phone number(818.562.7180), email(contact@brvbuildworksinc.example) , and website for potential clients to reach out.

The design should reflect the professionalism and strength of our industry, using a modern, clean layout with bold colors that align with construction and demolition themes. Images of past work or stock photos representing our services are encouraged.

Final deliverables should be print-ready (PDF) and digital-friendly formats. Looking forward to creative and impactful designs!

```html
<!DOCTYPE html>
<html lang="en">
<head>
<meta charset="utf-8">
<title>BRV Buildworks – Sales Brochure</title>
<link href="https://fonts.googleapis.com/css2?family=Poppins:wght@400;500;600;700;800&family=Oswald:wght@300;500&display=swap" rel="stylesheet">
<style>
:root{
  --blue:#1b75c4;
  --sky:#4aa8f0;
  --ink:#111;
  --black:#000;
  --paper:#fff;
  --grey:#6b6b6b;
  --stage:#c9c9c9;
  --sand:#c9a46e;
  --dusk:#e9b56a;
  --concrete:#a7adb3;
  --glass:#8fb4d9;
}
*{margin:0;padding:0;box-sizing:border-box}
html,body{width:907px;height:1200px;overflow:hidden}
body{background:var(--stage);font-family:"Poppins",sans-serif;color:var(--ink);position:relative}
.page{position:absolute;width:362px;height:468px;background:var(--paper);overflow:hidden}
.p-cover{left:74px;top:102px}
.p-services{left:490px;top:102px}
.p-scope{left:74px;top:632px}
.p-contact{left:490px;top:632px}
.abs{position:absolute}
.photo{position:absolute}
.brand{position:absolute;left:0;right:0;text-align:center;font-weight:800;color:var(--blue);letter-spacing:1px;line-height:1}
.brand small{display:block;font-weight:800;font-size:7px;letter-spacing:4px;margin-top:5px;color:var(--blue)}
.center{left:0;right:0;text-align:center}
/* cover */
.band{position:absolute;left:0;right:0;background:var(--blue)}
.cover-kicker{top:319px;font-size:15px;letter-spacing:2px;color:var(--paper);font-weight:400;line-height:1}
.cover-title{top:333px;font-size:22px;font-weight:700;color:#8fc8f5;line-height:22px}
.pill{position:absolute;background:var(--black);color:var(--paper);border-radius:6px;text-align:center;white-space:nowrap}
.cover-pill{left:100px;width:162px;top:382px;height:18px;font-size:10px;letter-spacing:1px;line-height:18px}
.cover-lede{top:406px;font-size:5.6px;color:var(--paper);font-weight:500;line-height:7px;padding:0 30px}
.cover-web{top:436px;font-size:8px;letter-spacing:2px;color:var(--paper);font-weight:600}
/* services */
.col-blue{position:absolute;left:0;top:0;width:220px;height:468px;background:var(--blue)}
.about{position:absolute;left:25px;top:25px;width:321px;height:91px;background:var(--black);border:2px solid var(--paper);border-right:0;border-bottom:0}
.h-sky{color:var(--sky);font-weight:700}
.tiny{font-size:4.6px;line-height:6.4px;color:var(--paper)}
.svc-h{position:absolute;left:25px;font-size:9.5px;color:var(--paper);font-weight:700}
.svc-p{position:absolute;left:25px;width:168px}
.frame-w{position:absolute;background:var(--paper)}
.rule{position:absolute;height:0;border-top:1px dotted rgba(255,255,255,.45)}
.foot{position:absolute;left:25px;right:20px;height:10px}
.foot .url{position:absolute;left:0;top:0;height:9px;padding:0 6px;border-radius:5px;background:var(--black);color:var(--paper);font-size:5.5px;line-height:9px;white-space:nowrap}
.foot .line{position:absolute;left:104px;right:6px;top:4px;border-top:1px solid #333}
.foot .num{position:absolute;right:0;top:0;width:8px;height:8px;border-radius:50%;background:var(--black);color:var(--paper);font-size:4.5px;text-align:center;line-height:8px}
/* scope */
.sec-h{position:absolute;font-weight:700;color:var(--grey);font-size:10px;line-height:10.5px}
.body{font-size:5.2px;line-height:6.5px;color:#222}
.types{position:absolute;left:158px;top:27px;width:179px;height:397px;background:var(--black)}
.type-h{position:absolute;left:32px;font-size:8px;font-weight:500;color:var(--paper)}
.type-h b{color:var(--sky);font-weight:700}
.type-icon{position:absolute;left:-8px;width:30px;height:18px;border-radius:0 9px 9px 0;background:#e8e8e8}
.type-icon i{position:absolute;right:2px;top:2px;width:14px;height:14px;border-radius:50%;background:var(--paper);border:1px solid var(--blue)}
.type-photo{position:absolute;left:32px;width:127px;height:51px;border:1.5px solid var(--paper)}
.type-p{position:absolute;left:32px;width:134px;font-size:4.8px;line-height:6.4px;color:var(--paper)}
.price-from{position:absolute;left:18px;top:292px;font-family:"Oswald",sans-serif;font-weight:300;font-size:15px;line-height:1}
.price-from b{font-weight:500;color:var(--blue);font-size:25px}
.price-from sup{font-size:11px;color:var(--blue);font-weight:500}
.inc{position:absolute;left:18px;top:322px;height:11px;padding:0 6px;border-radius:3px;background:#555;color:var(--paper);font-size:6px;line-height:11px}
.inc-item{position:absolute;left:18px;width:121px;height:24px;border-bottom:1px solid #bbb}
.inc-item svg{position:absolute;left:0;top:3px}
.inc-item span{position:absolute;left:22px;top:3px;font-size:6px;line-height:7.5px;font-weight:600}
/* contact */
.c-h{font-size:14px;letter-spacing:2.5px;line-height:14px;color:var(--black);font-weight:500}
.c-line{font-size:9.5px;color:var(--paper);line-height:10px}
.icons{position:absolute;left:96px;top:332px;width:170px;height:20px}
</style>
</head>
<body>

<section class="page p-cover">
  <div class="brand" style="top:30px;font-size:24px">BRV<small>BUILDWORKS</small></div>
  <div class="band" style="top:285px;bottom:0"></div>
  <div class="abs" style="left:25px;top:101px;width:303px;height:185px;background:var(--black)"></div>
  <div class="abs" style="left:35px;top:111px;width:281px;height:195px;background:var(--paper)"></div>
  <div class="photo" role="img" aria-label="Hillside excavation site with a compact excavator at sunset above the city" style="left:43px;top:119px;width:266px;height:179px;background:linear-gradient(180deg,var(--dusk) 0%,#cfa579 30%,var(--sand) 60%,#a87b4a 100%)"></div>
  <div class="abs center cover-kicker">LOS ANGELES BASED</div>
  <div class="abs center cover-title">DEMOLITION GRADING<br>&amp; STRUCTURAL CONCRETE</div>
  <div class="pill cover-pill">CONTRACTOR SERVICES</div>
  <p class="abs center cover-lede">Committed to excellence, we leverage cutting-edge technology and skilled craftsmanship to ensure the structural integrity and aesthetic appeal of every project we undertake.</p>
  <div class="abs center cover-web">www.brvbuildworksinc.example</div>
</section>

<section class="page p-services">
  <div class="col-blue"></div>
  <div class="about">
    <div class="photo" role="img" aria-label="Retaining wall construction site with excavator" style="left:6px;top:6px;width:95px;height:73px;border:1px solid var(--blue);background:linear-gradient(180deg,#6aa0d8 0%,#8a9a7a 35%,var(--concrete) 55%,var(--sand) 100%)"></div>
    <div class="abs h-sky" style="left:110px;top:7px;font-size:9.5px">ABOUT US</div>
    <p class="abs tiny" style="left:110px;top:21px;width:205px">BRV Buildworks is rooted in a deep understanding of the unique challenges presented by hillside properties, allowing us to deliver safe, efficient, and innovative solutions that meet the highest industry standards. Committed to excellence, we leverage cutting-edge technology and skilled craftsmanship to ensure the structural integrity and aesthetic appeal of every project we undertake. Our dedication to quality and customer satisfaction has established BRV Buildworks as a trusted partner in the dynamic landscape of residential construction in Southern California.</p>
  </div>
  <svg class="abs" style="left:25px;top:124px" width="20" height="20" viewBox="0 0 20 20" fill="none" stroke="#fff" stroke-width="1.3"><circle cx="13" cy="7" r="4"/><path d="M11 7l1.5 1.5L15 6"/><path d="M2 15l4-2h5l3-2M2 18h8l6-4"/></svg>
  <div class="abs" style="left:53px;top:127px;font-size:10px;font-weight:700;color:var(--black)">SERVICES WE OFFER</div>

  <div class="svc-h" style="top:153px">DEMOLITION</div>
  <p class="svc-p tiny" style="top:172px">At BRV Buildworks, our demolition services are designed to ensure the efficient and safe removal of structures while minimizing impact on the surrounding environment. We utilize advanced equipment and techniques to handle projects of any size, from residential buildings to large commercial sites. Our team of skilled professionals is trained to assess each project carefully, implementing effective strategies that prioritize safety and regulatory compliance.</p>
  <div class="frame-w" style="left:198px;top:145px;width:164px;height:88px"></div>
  <div class="photo" role="img" aria-label="Excavator demolishing on a wooded lot" style="left:202px;top:149px;width:142px;height:80px;background:linear-gradient(180deg,#6d7f4c 0%,#9a8a5a 45%,#b08a5a 100%)"></div>
  <div class="rule" style="left:25px;width:170px;top:235px"></div>

  <div class="svc-h" style="top:246px">GRADING</div>
  <p class="svc-p tiny" style="top:267px">BRV Buildworks specializes in comprehensive site grading and mass excavation and hauling services, ensuring that each project lays a solid foundation for future development. Our skilled team utilizes state-of-the-art equipment to effectively manage soil removal, leveling, and site preparation, significantly enhancing the efficiency of construction timelines. We prioritize precision and safety throughout the process, adhering to industry standards while minimizing environmental impact.</p>
  <div class="frame-w" style="left:198px;top:240px;width:164px;height:89px"></div>
  <div class="photo" role="img" aria-label="Graded hillside lot with long concrete retaining walls" style="left:202px;top:244px;width:142px;height:81px;background:linear-gradient(180deg,#5e93d4 0%,#8d9499 35%,#b9a27a 70%,var(--sand) 100%)"></div>
  <div class="rule" style="left:25px;width:170px;top:335px"></div>

  <div class="svc-h" style="top:354px">STRUCTURAL CONCRETE</div>
  <p class="svc-p tiny" style="top:374px">Our structural concrete and foundation division offers comprehensive solutions tailored to meet the diverse needs of our clients. We specialize in everything from slab-on-grade foundations to shoring and retaining walls, as well as hillside basements. Our dedicated team employs advanced techniques and high-quality materials to ensure stability, durability, and safety for all types of projects.</p>
  <div class="frame-w" style="left:198px;top:337px;width:164px;height:88px"></div>
  <div class="photo" role="img" aria-label="Aerial view of concrete foundation walls on a hillside lot" style="left:202px;top:341px;width:142px;height:80px;background:linear-gradient(160deg,#7c8a6a 0%,#c0c3c4 45%,#b39b74 100%)"></div>

  <div class="foot" style="top:436px"><span class="url">www.brvbuildworksinc.example</span><span class="line"></span><span class="num">1</span></div>
</section>

<section class="page p-scope">
  <div class="abs" style="left:241px;top:0;width:124px;height:27px;background:var(--blue)"></div>
  <div class="abs" style="left:337px;top:0;width:28px;height:112px;background:var(--blue)"></div>

  <svg class="abs" style="left:18px;top:26px" width="20" height="20" viewBox="0 0 20 20" fill="none" stroke="#222" stroke-width="1.3"><circle cx="10" cy="9" r="2.5"/><path d="M6 19v-4l4-3 4 3v4"/><circle cx="4" cy="4" r="2" stroke="#1b75c4"/><circle cx="16" cy="4" r="2" stroke="#1b75c4"/><circle cx="10" cy="2.5" r="1.6"/></svg>
  <div class="sec-h" style="left:41px;top:25px">PROJECT SCOPE<br>&amp; CAPABILITIES</div>
  <p class="abs body" style="left:18px;top:53px;width:124px">BRV Buildworks is a leading construction firm established in 2019, driven by a commitment to excellence and innovation in the building industry. With a team of seasoned professionals, we specialize in delivering high-quality residential and commercial projects tailored to meet our clients' specific needs.</p>
  <div class="abs" style="left:18px;top:106px;font-size:11px;font-weight:800;color:var(--blue)">OUR MISSION</div>
  <p class="abs body" style="left:18px;top:124px;width:124px">Centers on building lasting relationships with our clients, ensuring open communication and collaboration throughout each phase of the construction process. We prioritize safety, sustainability, and efficiency, employing the latest industry practices and technologies to enhance project outcomes.</p>
  <p class="abs body" style="left:18px;top:182px;width:124px"><b>At BRV Buildworks, we take pride in our ability to transform visions into reality,</b> providing not just structures but spaces that inspire and endure. Our diverse portfolio showcases our versatility and dedication to quality craftsmanship, making us a trusted partner in the construction landscape.</p>
  <div class="abs" style="left:18px;top:242px;width:127px;border-top:1px dotted #888"></div>

  <svg class="abs" style="left:18px;top:253px" width="18" height="20" viewBox="0 0 18 20"><circle cx="12" cy="6" r="5" fill="#1b75c4"/><text x="12" y="8.5" font-size="7" fill="#fff" text-anchor="middle" font-family="Poppins">$</text><path d="M1 11h4v8H1zM6 12l3-2 2 1v8H6z" fill="#111"/></svg>
  <div class="sec-h" style="left:40px;top:251px">PRICING<br>INFORMATION</div>
  <div class="abs" style="left:18px;top:278px;font-size:10.5px;font-weight:700">Demolition Services</div>
  <div class="price-from">START AT <sup>$</sup><b>20,000</b></div>
  <div class="inc">THIS PRICE INCLUDES</div>
  <div class="inc-item" style="top:340px">
    <svg width="16" height="16" viewBox="0 0 16 16" fill="none" stroke="#1b75c4" stroke-width="1.2"><path d="M1 14h9v-4H1zM3 10V7l5-5 3 3"/><circle cx="12" cy="11" r="2.5" stroke="#222"/></svg>
    <span>Complete demolition of structure</span></div>
  <div class="inc-item" style="top:367px">
    <svg width="16" height="16" viewBox="0 0 16 16" fill="none" stroke="#1b75c4" stroke-width="1.2"><path d="M1 12h10V6H1zM11 8h3l1 3v1h-4"/><circle cx="4" cy="13" r="1.5" stroke="#222"/><circle cx="12" cy="13" r="1.5" stroke="#222"/></svg>
    <span>Safe debris removal &amp;<br>hauling</span></div>
  <div class="inc-item" style="top:394px;border-bottom:0">
    <svg width="16" height="16" viewBox="0 0 16 16" fill="none" stroke="#1b75c4" stroke-width="1.2"><path d="M8 1a4 4 0 014 4c0 3-4 7-4 7S4 8 4 5a4 4 0 014-4z"/><circle cx="8" cy="5" r="1.4"/><path d="M1 15l3-4h8l3 4z" stroke="#222"/></svg>
    <span>Site preparation for new construction.</span></div>

  <div class="types">
    <div class="abs" style="left:14px;top:10px;font-size:10px;font-weight:700;color:var(--sky);line-height:11px">THE TYPE OF PROJECTS<br><span style="font-weight:400;color:var(--paper)">WE HANDLE</span></div>

    <div class="type-icon" style="top:38px"><i></i></div>
    <div class="type-h" style="top:42px"><b>RESIDENTIAL</b> PROJECTS</div>
    <div class="type-photo" role="img" aria-label="New residential foundation slab in front of houses" style="top:59px;background:linear-gradient(180deg,#9db5cf 0%,#8a7f72 45%,#b7bcc0 100%)"></div>
    <p class="type-p" style="top:117px">Lorem ipsum dolor sit amet, consectetur adipiscing elit, sed do eiusmod tempor incididunt ut labore et dolore magna aliqua. Quis ipsum suspendisse ultrices gravida. Risus commodo viverra maecenas accumsan lacus vel facilisis.</p>

    <div class="type-icon" style="top:154px"><i></i></div>
    <div class="type-h" style="top:158px"><b>COMMERCIAL</b> PROJECTS</div>
    <div class="type-photo" role="img" aria-label="Engineer reviewing plans inside a modern glass building" style="top:176px;background:linear-gradient(120deg,#e9eef2 0%,#b7c6d2 50%,#5d6f80 100%)"></div>
    <p class="type-p" style="top:235px">Lorem ipsum dolor sit amet, consectetur adipiscing elit, sed do eiusmod tempor incididunt ut labore et dolore magna aliqua. Quis ipsum suspendisse ultrices gravida. Risus commodo viverra maecenas accumsan lacus vel facilisis.</p>

    <div class="type-icon" style="top:272px"><i></i></div>
    <div class="type-h" style="top:276px"><b>INDUSTRIAL</b> PROJECTS</div>
    <div class="type-photo" role="img" aria-label="Glass facade of an industrial building in sunlight" style="top:291px;background:linear-gradient(110deg,#3c62a8 0%,var(--glass) 55%,#f3efe4 100%)"></div>
    <p class="type-p" style="top:353px">Lorem ipsum dolor sit amet, consectetur adipiscing elit, sed do eiusmod tempor incididunt ut labore et dolore magna aliqua. Quis ipsum suspendisse ultrices gravida. Risus commodo viverra maecenas accumsan lacus vel facilisis.</p>
  </div>

  <div class="foot" style="top:440px;left:18px"><span class="url">www.brvbuildworksinc.example</span><span class="line"></span><span class="num">2</span></div>
</section>

<section class="page p-contact">
  <div class="brand" style="top:58px;font-size:19px">BRV<small style="font-size:6px">BUILDWORKS</small></div>
  <div class="abs" style="left:60px;top:109px;width:246px;height:156px;background:var(--black)"></div>
  <div class="photo" role="img" aria-label="Aerial view of foundation formwork on a graded lot" style="left:68px;top:117px;width:230px;height:139px;background:linear-gradient(150deg,#d7c5a4 0%,#bfa67f 50%,#8e7a5c 100%)"></div>
  <div class="band" style="top:287px;bottom:0"></div>
  <div class="abs center c-h" style="top:302px">CONTACT US FOR<br><b style="font-weight:600">MORE INFORMATION</b></div>
  <svg class="icons" viewBox="0 0 170 20">
    <g stroke="#fff" stroke-width="1"><path d="M0 8h30M4 10h26M0 12h30M140 8h30M140 10h26M140 12h30"/></g>
    <g fill="#fff"><circle cx="41" cy="10" r="9"/><circle cx="67" cy="10" r="9"/><circle cx="93" cy="10" r="9"/><circle cx="119" cy="10" r="9"/></g>
    <path d="M37 6c0 5 3 8 8 8l1-2-2-1-1 1c-2-1-3-2-4-4l1-1-1-2z" fill="#111"/>
    <path d="M67 4a3.5 3.5 0 013.5 3.5C70.5 10 67 14 67 14s-3.5-4-3.5-6.5A3.5 3.5 0 0167 4z" fill="#111"/><circle cx="67" cy="7.5" r="1.3" fill="#fff"/>
    <rect x="88" y="6.5" width="10" height="7" fill="#111"/><path d="M88 6.5l5 4 5-4" stroke="#fff" stroke-width=".8" fill="none"/>
    <g stroke="#111" stroke-width="1" fill="none"><circle cx="119" cy="10" r="5"/><ellipse cx="119" cy="10" rx="2" ry="5"/><path d="M114 10h10"/></g>
  </svg>
  <div class="abs center c-line" style="top:363px">818.562.7180</div>
  <div class="abs center c-line" style="top:383px">Lorem ipsum dolor sit<br>amet, consectetur</div>
  <div class="abs center c-line" style="top:413px">contact@brvbuildworksinc.example</div>
  <div class="abs center c-line" style="top:437px">www.brvbuildworksinc.example</div>
</section>

</body>
</html>
```